Business Card: RW Office Partners - Your tidy answer finder

Business Name: RW Office Partners
Website: www.rwofficepartners.com.au
Email: marisol@rwofficepartners.com.au
Mobile: 61 487 902 346
Facebook: @rwofficepartners
Instrgram: @rwofficepartners

Brading Colours:
HEX
#986474
#ddccd3
#7a8498
#c9d8e4
#000000
#ffffff

Tag Line: Your organised problem solver

Link to DRAFT website:
https://helpdeskhub.sitebuilderx.com/rw-office-partners

About Page from the website:
My name is Marisol Bramwell, and I would love to assist you to become more productive in your day to day and achieve your business and personal goals.
My mission is to give you time, time to work on the important tasks of your business or to be able to spend more time with your family. I will take on the tasks you don’t have time for, don’t know well or simply don’t like to do.
I have an extensive background in Administration, Tender Coordination, Document Control, WHS and Quality Management working primarily in the Construction, Mining and Corporate World.
I am passionate about being organised, having order and making things in your life (and mine) easier! I love to watch something unfold and grow into something amazing! I am known for being the go-to problem solver, the organiser of all things, producing high standards of work even under pressure. I’m also a confident communicator, and I understand that you’re busy running your business.

Target Market(s)

Small to Medium Business who require assistance in their business by a virtual assistant.

Industry/Entity Type

Virtual Assistant

Contact Information for Business Card

Mobile: 61 487 902 346

Font styles to use
Sans Serif

Colors
ffffff

Requirements
Must have
• Branding Colours as outlined.
Contact Details as outlined.
Logo as provided.
Proper contact details - mobile, facebook, instragm, website.
Simple, Elegant, very clean looking.
Should not have
• Note cute with pictures.
Not too girly as still want to market to construction companies.

```html
<!DOCTYPE html>
<html lang="en">
<head>
<meta charset="utf-8">
<title>RW Office Partners – Business Card</title>
<link rel="stylesheet" href="https://fonts.googleapis.com/css2?family=Arimo:wght@400&display=swap">
<style>
  :root{
    --mauve:#986474;
    --slate:#7a8498;
    --white:#ffffff;
    --backdrop:#e6e6e8;
  }
  html,body{margin:0;padding:0;overflow:hidden;}
  body{
    width:1200px;height:1022px;
    background:var(--backdrop);
    display:flex;align-items:center;justify-content:center;
    font-family:"Arimo",Arial,sans-serif;
  }
  .card{
    position:relative;
    width:1000px;height:572px;
    background:var(--white);
    box-shadow:0 10px 30px rgba(0,0,0,.12);
    overflow:hidden;
  }
  .brand{
    position:absolute;top:62px;right:60px;
    display:flex;align-items:center;gap:14px;
  }
  .brand-mark{width:26px;height:26px;background:var(--mauve);}
  .brand-name{font-size:34px;line-height:1;color:var(--slate);letter-spacing:.5px;white-space:nowrap;}
  .contacts{
    position:absolute;left:70px;top:140px;
    margin:0;padding:0;list-style:none;
  }
  .contact{
    display:flex;align-items:center;gap:18px;
    height:46px;
    font-size:21px;color:var(--slate);
    white-space:nowrap;
  }
  .contact svg{width:34px;height:34px;flex:none;}
  .footer-band{
    position:absolute;left:0;bottom:0;
    width:790px;height:70px;
    background:var(--slate);
    border-top-right-radius:40px;
  }
  .corner-block{
    position:absolute;right:0;bottom:0;
    width:165px;height:112px;
    background:var(--mauve);
    border-top-left-radius:40px;
  }
</style>
</head>
<body>
  <div class="card">
    <div class="brand">
      <span class="brand-mark"></span>
      <span class="brand-name">RW Office Partners</span>
    </div>

    <ul class="contacts">
      <li class="contact">
        <svg viewBox="0 0 34 34" fill="none" stroke="var(--slate)" stroke-width="2"><circle cx="17" cy="17" r="14"/><ellipse cx="17" cy="17" rx="6" ry="14"/><line x1="3" y1="17" x2="31" y2="17"/><line x1="5" y1="10" x2="29" y2="10"/><line x1="5" y1="24" x2="29" y2="24"/></svg>
        <span>www.rwofficepartners.com.au</span>
      </li>
      <li class="contact">
        <svg viewBox="0 0 34 34" fill="none" stroke="var(--slate)" stroke-width="2"><rect x="3" y="8" width="28" height="19"/><polyline points="3,8 17,20 31,8"/><line x1="3" y1="27" x2="14" y2="17"/><line x1="31" y1="27" x2="20" y2="17"/></svg>
        <span>marisol@rwofficepartners.com.au</span>
      </li>
      <li class="contact">
        <svg viewBox="0 0 34 34" fill="none" stroke="var(--slate)" stroke-width="2"><rect x="9" y="2" width="16" height="30" rx="2"/><line x1="14" y1="5" x2="20" y2="5"/><circle cx="17" cy="28" r="1.2" fill="var(--slate)"/></svg>
        <span>61 487 902 346</span>
      </li>
      <li class="contact">
        <svg viewBox="0 0 34 34" fill="none" stroke="var(--slate)" stroke-width="2"><rect x="5" y="5" width="24" height="24" rx="3"/></svg>
        <span>@rwofficepartners</span>
      </li>
      <li class="contact">
        <svg viewBox="0 0 34 34" fill="none" stroke="var(--slate)" stroke-width="2"><circle cx="17" cy="17" r="12"/></svg>
        <span>@rwofficepartners</span>
      </li>
      <li class="contact">
        <svg viewBox="0 0 34 34" fill="none" stroke="var(--slate)" stroke-width="3" stroke-linecap="round"><path d="M14 20 L20 14"/><path d="M12 16 L8 20 a4.5 4.5 0 0 0 6 6 L18 22"/><path d="M22 18 L26 14 a4.5 4.5 0 0 0 -6 -6 L16 12"/></svg>
        <span>https://helpdeskhub.sitebuilderx.com/rw-office-partners</span>
      </li>
    </ul>

    <div class="footer-band" aria-hidden="true"></div>
    <div class="corner-block" aria-hidden="true"></div>
  </div>
</body>
</html>
```